Cover Art Needed For Digital Single Release

We are looking to have the cover art designed for a new song called "Paper Lanterns". You will find the track attached below in a private TuneVault link so that you can have a listen.
We are thinking of keeping the artwork fairly simple but still want it to catch your eye. Maybe using the song title and artist’s name in a colorful and creative way. (A well-designed font with a bold color scheme, or even something like a mosaic style art piece featuring the title).
We completely welcome any and all creative visions you might have, even if it strays away from the examples given above.
Thank you in advance for your submissions, and we are excited to collaborate with you!
"Paper Lanterns" by Marcus Holloway
https://tunevault.example/marcusxyz/paper-lanterns/s-r7Tq2wLmNcx
Target Market(s)
Teens/Young Adults
Industry/Entity Type
Music
Requirements
Must have
- An eye-catching design
Should not have
- Please do not rely heavily on stock images. We prefer an original design/concept.

```html
<!DOCTYPE html>
<html lang="en">
<head>
<meta charset="utf-8">
<title>Paper Lanterns – Elian Varga</title>
<link rel="stylesheet" href="https://fonts.googleapis.com/css2?family=Questrial&display=swap">
<style>
  :root {
    --slate-blue: #6a86a8;
    --deep-slate: #4f6b93;
    --violet: #8b3fa6;
    --mandala-dark: #3a2146;
    --mandala-mid: #6b2a6e;
    --mandala-pink: #e0409a;
    --mandala-cream: #f1e6c6;
    --halo: #a9d3c4;
    --title-white: #ffffff;
  }
  * { margin: 0; padding: 0; box-sizing: border-box; }
  html, body { width: 1200px; height: 1200px; overflow: hidden; }
  body { background: var(--deep-slate); }
  .cover {
    position: relative;
    width: 1200px;
    height: 1200px;
    overflow: hidden;
  }
  .cover-artwork {
    position: absolute;
    inset: 0;
    width: 1200px;
    height: 1200px;
  }
  .title-block {
    position: absolute;
    right: 40px;
    bottom: 20px;
    display: flex;
    flex-direction: column;
    align-items: stretch;
    color: var(--title-white);
    font-family: "Questrial", sans-serif;
  }
  .song-title {
    font-size: 106px;
    line-height: 0.9;
    font-weight: 400;
    text-transform: uppercase;
    text-align: right;
    letter-spacing: 0.03em;
    margin-right: -0.03em;
  }
  .title-rule {
    width: 100%;
    height: 3px;
    background: var(--title-white);
    margin: 16px 0 8px;
  }
  .artist-name {
    font-size: 32px;
    line-height: 1;
    letter-spacing: 0.38em;
    margin-right: -0.38em;
    text-align: right;
    text-transform: uppercase;
    white-space: nowrap;
  }
</style>
</head>
<body>
  <main class="cover">
    <svg class="cover-artwork" viewBox="0 0 1200 1200" xmlns="http://www.w3.org/2000/svg">
      <defs>
        <radialGradient id="backdrop-gradient" cx="50%" cy="50%" r="75%">
          <stop offset="0%" stop-color="#7a6aa8"/>
          <stop offset="45%" stop-color="var(--slate-blue)"/>
          <stop offset="80%" stop-color="var(--deep-slate)"/>
          <stop offset="100%" stop-color="var(--violet)"/>
        </radialGradient>
        <radialGradient id="mandala-gradient" cx="50%" cy="50%" r="50%">
          <stop offset="0%" stop-color="var(--mandala-dark)"/>
          <stop offset="12%" stop-color="var(--mandala-pink)"/>
          <stop offset="28%" stop-color="var(--mandala-cream)"/>
          <stop offset="50%" stop-color="#d6a7b8"/>
          <stop offset="58%" stop-color="var(--mandala-mid)"/>
          <stop offset="100%" stop-color="var(--mandala-dark)"/>
        </radialGradient>
      </defs>
      <rect class="backdrop" width="1200" height="1200" fill="url(#backdrop-gradient)"
            role="img" aria-label="Kaleidoscopic lattice pattern in slate blue and violet"/>
      <circle class="mandala-halo" cx="600" cy="600" r="425" fill="var(--halo)" opacity="0.45"/>
      <circle class="mandala" cx="600" cy="600" r="390" fill="url(#mandala-gradient)"
              role="img" aria-label="Central flower mandala of dotted purple petals around a cream and pink core"/>
    </svg>

    <header class="title-block">
      <h1 class="song-title">Paper<br>Lanterns</h1>
      <div class="title-rule"></div>
      <p class="artist-name">Elian Varga</p>
    </header>
  </main>
</body>
</html>
```